Fully Functional Wix Website, Not Just Images

Please read all instructions carefully. This is NOT merely a design project where the artist will deliver static images. This project requires that the designer build a fully functional SEO optimized website within Wix then transfer full ownership to me. See attached "instructions for design" file. I have wix for other websites. Only wix is acceptable. Do not submit more than 1 design per designer. If you submit more than 1 design I will award to someone else.

Target Market(s)

see attachments and brisvale482.com

Industry/Entity Type

Coding

Coded - Design and coding required

Number of Pages Required

4 page

Font styles to use
Other font styles liked:
• see attachments and brisvale482.com

Requirements
Must have
Nice to have
Should not have

```html
<!DOCTYPE html>
<html lang="en">
<head>
<meta charset="utf-8">
<title>Captain Rowan's Boat Training &amp; Charters</title>
<link href="https://fonts.googleapis.com/css2?family=DM+Serif+Display:ital@0;1&family=Marcellus&family=Montserrat:wght@400;500;600;700&display=swap" rel="stylesheet">
<style>
:root{
  --navy:#0f2b46;
  --navy-deep:#0c2338;
  --gold:#d4a514;
  --cream:#f3eedd;
  --mauve:#cbc3c3;
  --ink:#1d2a38;
  --white:#ffffff;
  --card:#f6f5f2;
}
*{box-sizing:border-box;margin:0;padding:0}
html,body{width:1200px;height:3333px;overflow:hidden}
body{position:relative;font-family:"Montserrat",sans-serif;color:var(--ink);background:var(--white)}
section,footer{position:absolute;left:0;width:1200px}
.abs{position:absolute}
.serif{font-family:"Marcellus",serif}
.display{font-family:"DM Serif Display",serif}
.btn{position:absolute;display:flex;align-items:center;justify-content:center;font-weight:600;font-size:11px;letter-spacing:.4px;text-transform:uppercase}
.btn-gold{background:var(--gold);color:var(--white)}
.btn-line{border:2px solid var(--navy);color:var(--navy);border-radius:3px}

/* hero */
.hero{top:0;height:547px}
.hero-photo{position:absolute;inset:0;background:linear-gradient(100deg,#2e3a2a 0%,#3d4c3a 28%,#4e6476 52%,#8fa3b4 70%,#2d4a62 100%)}
.hero-shade{position:absolute;inset:0;background:linear-gradient(180deg,rgba(10,25,40,.15),rgba(10,25,40,.45))}
.brand-badge{position:absolute;left:116px;top:16px;width:100px;height:100px;border-radius:50%;background:var(--navy);border:4px solid var(--gold);display:flex;align-items:center;justify-content:center;text-align:center;color:var(--white);font-size:10px;font-weight:700;line-height:1.3;padding:10px}
.nav{position:absolute;top:58px;left:512px;display:flex;gap:15px;font-size:11px;font-weight:600;color:var(--white);letter-spacing:.8px}
.nav-cta{left:951px;top:51px;width:132px;height:29px}
.hero-title{position:absolute;left:116px;top:176px;font-family:"DM Serif Display",serif;font-size:72px;line-height:64px;color:var(--white);font-weight:400}
.hero-text{position:absolute;left:118px;top:332px;width:430px;font-size:12.5px;line-height:19px;color:var(--white);font-weight:500}
.hero-b1{left:121px;top:438px;width:168px;height:31px}
.hero-b2{left:305px;top:438px;width:149px;height:31px;border:1.5px solid var(--white);color:var(--white);border-radius:2px}

/* guides */
.guides{top:547px;height:691px;background:var(--cream)}
.eyebrow{position:absolute;width:100%;text-align:center;font-size:10.5px;color:var(--gold);font-weight:600;letter-spacing:.3px}
.guides-title{position:absolute;top:60px;width:100%;text-align:center;font-size:60px;color:var(--navy);font-weight:400}
.guides-sub{position:absolute;top:131px;width:100%;text-align:center;font-size:13px;color:var(--ink)}
.book{position:absolute;top:186px;width:309px;height:377px;background:linear-gradient(180deg,#1b4fa0 0%,#2a6ad0 40%,#5b7fa8 70%,#1c2d4a 100%)}
.book-2{background:linear-gradient(180deg,#14325f 0%,#2a5ea8 45%,#6c8db3 70%,#172640 100%)}
.book-3{background:linear-gradient(180deg,#1d55b8 0%,#3b78d4 45%,#8aa4be 72%,#1a2b48 100%)}
.store-btn{left:426px;top:595px;width:362px;height:47px;background:var(--navy);color:var(--white);font-size:11.5px;border-radius:2px;gap:10px}
.store-note{position:absolute;top:650px;width:100%;text-align:center;font-size:10px;color:var(--ink);font-weight:500}

/* about */
.about{top:1238px;height:612px;background:var(--mauve)}
.about-photo{position:absolute;left:0;top:0;width:620px;height:612px;background:radial-gradient(ellipse at 55% 55%,#d9dbe0 0%,#b9bcc4 40%,#c7bfc0 75%)}
.about-title{position:absolute;left:652px;top:66px;font-size:46px;line-height:52px;color:var(--navy);font-weight:400}
.about-text{position:absolute;left:653px;width:420px;font-size:12.5px;line-height:19px;color:var(--ink)}
.about-btn{left:652px;top:446px;width:149px;height:31px;font-size:10.5px}

.creds{position:absolute;left:116px;top:1764px;width:968px;height:165px;background:var(--navy);display:flex;padding:26px 0 0 30px}
.cred{width:194px;color:var(--white)}
.cred svg{display:block;margin:0 0 12px 30px}
.cred h3{font-size:13.5px;font-weight:600;margin-bottom:5px}
.cred p{font-size:9.5px;line-height:12.5px;width:140px}

.motto{position:absolute;top:1955px;width:100%;text-align:center;font-size:34px;color:var(--navy)}
.motto-by{position:absolute;top:2021px;width:100%;text-align:center;font-size:10.5px;color:var(--ink);font-weight:500}

/* reviews */
.reviews{top:2072px;height:540px;background:var(--cream);border-radius:80px 80px 0 0}
.reviews-title{position:absolute;left:110px;top:48px;font-size:80px;line-height:66px;color:var(--navy);letter-spacing:1px;font-weight:400}
.reviews-sub{position:absolute;left:118px;top:200px;font-size:13.5px;color:var(--ink);font-weight:500}
.rope{position:absolute;left:846px;top:0;width:12px;height:518px;background:linear-gradient(180deg,#c9a94e,#e0c56f,#c9a94e)}
.reviews-btn{left:934px;top:120px;width:149px;height:30px;font-size:10.5px}
.review{position:absolute;top:264px;width:309px;height:186px;background:var(--card);padding:18px 48px;font-family:Georgia,serif}
.review .who{display:flex;align-items:center;gap:10px}
.avatar{width:30px;height:30px;border-radius:50%;background:#e25a35}
.avatar.b{background:#7d7466}.avatar.c{background:#8c6b4d}
.who b{font-size:11px;color:#222}
.who small{display:block;font-size:9.5px;color:#999}
.stars{color:#f2b400;font-size:15px;letter-spacing:1px;margin:10px 0 6px}
.review p{font-size:11.5px;line-height:17px;color:#333}
.source{font-family:"Montserrat",sans-serif;font-size:16px;font-weight:600;color:#5b7fc4;margin-top:8px}
.arrow{position:absolute;top:338px}

/* services */
.services{top:2590px;height:498px}
.services-bg{position:absolute;inset:0;background:linear-gradient(180deg,#e6edf3 0%,#c3d3e0 45%,#a7bccd 100%)}
.services-title{position:absolute;left:116px;top:40px;font-size:58px;color:var(--navy);font-weight:400}
.services-sub{position:absolute;left:117px;top:110px;font-size:13.5px;color:var(--ink);font-weight:500}
.services-btn{left:934px;top:58px;width:149px;height:30px;font-size:10.5px}
.svc{position:absolute;top:170px;width:228px;height:215px;background:var(--white);text-align:center;padding-top:18px}
.svc svg{display:block;margin:0 auto 10px}
.svc h3{font-size:17px;font-weight:600;color:var(--navy);margin-bottom:10px}
.svc p{font-size:11px;line-height:14.5px;color:var(--ink);width:170px;margin:0 auto}
.svc a{display:block;margin-top:14px;font-size:11px;font-weight:600;color:var(--navy);text-decoration:underline}
.tagline{position:absolute;top:424px;width:100%;text-align:center;font-family:"DM Serif Display",serif;font-style:italic;font-size:25px;color:var(--navy)}

/* footer */
.footer{top:3088px;height:245px;background:linear-gradient(180deg,#1c3c5c,var(--navy-deep));color:var(--white)}
.footer .brand-badge{left:164px;top:27px;width:127px;height:127px;font-size:12px}
.socials{position:absolute;left:171px;top:160px;display:flex;gap:8px}
.socials span{width:30px;height:30px;border-radius:50%;border:2px solid var(--white)}
.f-head{position:absolute;top:46px;font-size:11px;font-weight:500;letter-spacing:.8px}
.f-links{position:absolute;left:662px;top:72px;font-size:11px;line-height:18.8px}
.contact-row{position:absolute;left:880px;display:flex;align-items:center;gap:14px;font-size:12px}
.contact-row .ic{width:28px;height:28px;border-radius:50%;border:1.5px solid var(--white);display:flex;align-items:center;justify-content:center}
.copy{position:absolute;top:212px;width:100%;text-align:center;font-size:10.5px}
</style>
</head>
<body>

<section class="hero">
  <div class="hero-photo" role="img" aria-label="Luxury motor yacht on calm water beside a green wooded headland, with the script line Training Today, Confidence Tomorrow"></div>
  <div class="hero-shade"></div>
  <div class="brand-badge">Captain Rowan's Boat Training &amp; Charters</div>
  <nav class="nav"><span>HOME</span><span>SERVICES</span><span>BOATING AIDS</span><span>GALLERY</span><span>ABOUT</span><span>CONTACT</span></nav>
  <div class="btn btn-gold nav-cta">Book a Charter</div>
  <h1 class="hero-title">Confidence<br>at the Helm</h1>
  <p class="hero-text">Whether You're New To Boating Or Ready To Build Real Confidence Behind The Wheel, Captain Rowan's Boat Training &amp; Charters, LLC Helps You Train, Handle, And Command Your Own Boat With Skill.</p>
  <div class="btn btn-gold hero-b1">Explore Our Charters</div>
  <div class="btn hero-b2">View Boat Training</div>
</section>

<section class="guides">
  <p class="eyebrow" style="top:40px">KNOWLEDGE FOR A BETTER BOATING TOMORROW</p>
  <h2 class="guides-title serif">Published Guides</h2>
  <p class="guides-sub">Practical Guidance. Real-world Insights. A Safer, Smarter You.</p>
  <div class="book" style="left:116px" role="img" aria-label="Book cover: Steady Course: Buying Smart, a guide to choosing a first boat, by Captain Rowan T. Delacourt"></div>
  <div class="book book-2" style="left:444px" role="img" aria-label="Book cover: Steady Course: Keeping Ready, a guide to storage, upkeep and safety, by Captain Rowan T. Delacourt"></div>
  <div class="book book-3" style="left:771px" role="img" aria-label="Book cover: Steady Course: Planning Passages, a guide to planning trips, by Captain Rowan T. Delacourt"></div>
  <div class="btn store-btn"><span style="width:14px;height:14px;border-radius:50%;background:var(--white)"></span>View the Steady Course Series on Pagewell
    <svg width="8" height="12" viewBox="0 0 8 12"><path d="M1 1l5 5-5 5" stroke="#fff" stroke-width="1.5" fill="none"/></svg></div>
  <p class="store-note">Visit Captain Rowan's Pagewell Press Author</p>
</section>

<section class="about">
  <div class="about-photo" role="img" aria-label="Portrait of Captain Rowan in a light grey uniform shirt with a flag patch"></div>
  <h2 class="about-title serif">Experience.<br>Knowledge.<br>A Safer Tomorrow.</h2>
  <p class="about-text" style="top:246px">I'm Captain Rowan Delacourt — a U.S. Coast Guard licensed Master Captain and National Safe Helm Council Certified Instructor, offering hands-on training, deliveries, and captaining services throughout the Harbor Bay area.</p>
  <p class="about-text" style="top:340px">A retired Army Master Sergeant with more than 23 years training and educating adults, I bring the same patience and structure to every session on the water — helping boaters build real, lasting confidence at the helm.</p>
  <div class="btn btn-line about-btn">More About Me</div>
</section>

<div class="creds">
  <div class="cred">
    <svg width="54" height="40" viewBox="0 0 54 40" fill="none" stroke="#fff" stroke-width="2"><ellipse cx="27" cy="14" rx="20" ry="9"/><path d="M9 18v8h36v-8M7 30h40"/></svg>
    <h3>Licensed Captain</h3><p>U.S. Coast Guard licensed Master Captain with Assistance Towing Endorsement</p>
  </div>
  <div class="cred">
    <svg width="54" height="40" viewBox="0 0 54 40" fill="none" stroke="#fff" stroke-width="2"><rect x="18" y="2" width="30" height="20"/><circle cx="14" cy="20" r="4"/><path d="M6 38v-10h16v10M22 26l10-8"/></svg>
    <h3>Certified Instructor</h3><p>National Safe Helm Council Certified Instructor</p>
  </div>
  <div class="cred">
    <svg width="54" height="40" viewBox="0 0 54 40" fill="none" stroke="#fff" stroke-width="2"><path d="M27 2l6 12 13 2-9 9 2 13-12-6-12 6 2-13-9-9 13-2z"/></svg>
    <h3>Veteran Owned</h3><p>Retired Army Master Sergeant with over 23 years training and educating adults</p>
  </div>
  <div class="cred">
    <svg width="54" height="40" viewBox="0 0 54 40" fill="none" stroke="#fff" stroke-width="2"><rect x="10" y="14" width="34" height="22" rx="3"/><path d="M20 14v-6h14v6M10 24h34"/></svg>
    <h3>Founder &amp; Operator</h3><p>Captain Rowan's Boat Training &amp; Charters, LLC</p>
  </div>
  <div class="cred">
    <svg width="64" height="40" viewBox="0 0 64 40" fill="none" stroke="#fff" stroke-width="2"><path d="M4 22h56l-8 12H12z"/><path d="M16 22v-10h30l6 10M22 12v10M32 12v10M40 12v10"/></svg>
    <h3>Trains on Your Boat</h3><p>Captain Rowan's Boat Training &amp; Charters, LLC</p>
  </div>
</div>

<p class="motto serif">“Good Boaters Make Brighter Tomorrows”</p>
<p class="motto-by">— Captain Rowan's Boat Training &amp; Charters, LLC</p>

<section class="reviews">
  <div class="rope" role="img" aria-label="Hanging gold rope tied in a knot"></div>
  <h2 class="reviews-title display">What our<br>customers say</h2>
  <p class="reviews-sub">Trusted by Our Customers, Proven by Their Experiences</p>
  <div class="btn btn-line reviews-btn">View All Reviews</div>
  <svg class="arrow" style="left:90px" width="10" height="16" viewBox="0 0 10 16"><path d="M8 1L2 8l6 7" stroke="#1d2a38" stroke-width="2" fill="none"/></svg>
  <svg class="arrow" style="left:1097px" width="10" height="16" viewBox="0 0 10 16"><path d="M2 1l6 7-6 7" stroke="#1d2a38" stroke-width="2" fill="none"/></svg>
  <div class="review" style="left:116px">
    <div class="who"><span class="avatar"></span><div><b>Dale Pruitt</b><small>3 days ago</small></div></div>
    <div class="stars">★★★★★</div>
    <p>Really good training, I would recommend Capt. Rowan to any new boat owner!</p>
    <div class="source">Reviewly</div>
  </div>
  <div class="review" style="left:444px">
    <div class="who"><span class="avatar b"></span><div><b>Norah Velling</b><small>1 month ago</small></div></div>
    <div class="stars">★★★★★</div>
    <p>Captain Rowan doesn't only have a cool name. He is amazing at what he does. His level of patience,…</p>
    <p style="color:#999">Read more</p>
    <div class="source">Reviewly</div>
  </div>
  <div class="review" style="left:771px">
    <div class="who"><span class="avatar c"></span><div><b>Victor Salenko</b><small>1 month ago</small></div></div>
    <div class="stars">★★★★★</div>
    <p>Captain Rowan was safe, attentive and an all around nice guy. Can't wait to rebook</p>
    <div class="source">Reviewly</div>
  </div>
</section>

<section class="services">
  <div class="services-bg" role="img" aria-label="Soft view of open sea from the bow of a boat with a person relaxing on deck"></div>
  <h2 class="services-title serif">Our Services</h2>
  <p class="services-sub">On The Water and Beyond</p>
  <div class="btn btn-line services-btn">View All Services</div>
  <svg class="abs" style="left:94px;top:272px" width="10" height="16" viewBox="0 0 10 16"><path d="M8 1L2 8l6 7" stroke="#1d2a38" stroke-width="2" fill="none"/></svg>
  <svg class="abs" style="left:1093px;top:272px" width="10" height="16" viewBox="0 0 10 16"><path d="M2 1l6 7-6 7" stroke="#1d2a38" stroke-width="2" fill="none"/></svg>
  <div class="svc" style="left:116px">
    <svg width="90" height="64" viewBox="0 0 90 64" fill="none" stroke="#d4a514" stroke-width="2.5"><path d="M4 40h82l-10 14H14z"/><path d="M18 40V28h46l8 12M30 28v-8h22v8"/></svg>
    <h3>Boat Training</h3><p>Hands-on Instruction Aboard Your Own Boat, At Your Own Dock.</p><a>LEARN MORE</a>
  </div>
  <div class="svc" style="left:363px">
    <svg width="90" height="64" viewBox="0 0 90 64" fill="none" stroke="#d4a514" stroke-width="2.5"><path d="M25 18h40l-4-12H29zM25 18h40"/><path d="M20 62V46h50v16M35 46l10 10 10-10"/></svg>
    <h3>Captaining</h3><p>A Licensed Captain At The Helm So You Can Focus On The Day.</p><a>LEARN MORE</a>
  </div>
  <div class="svc" style="left:610px">
    <svg width="90" height="64" viewBox="0 0 90 64" fill="none" stroke="#d4a514" stroke-width="2.5"><rect x="18" y="14" width="40" height="32"/><path d="M58 24h14l10 12v10H58"/><circle cx="32" cy="50" r="5"/><circle cx="70" cy="50" r="5"/><path d="M4 22h10M8 30h10M4 38h10"/></svg>
    <h3>Deliveries</h3><p>Getting Your Boat Safely To Its Slip, On Schedule.</p><a>LEARN MORE</a>
  </div>
  <div class="svc" style="left:858px">
    <svg width="110" height="64" viewBox="0 0 110 64" fill="none" stroke="#d4a514" stroke-width="2.5"><path d="M4 30h90l-14 14H20z"/><path d="M40 30l10-12h26M20 52h80"/><circle cx="40" cy="52" r="5"/><circle cx="80" cy="52" r="5"/></svg>
    <h3>Boating Aids</h3><p>Hands-on Instruction Aboard Your Own Boat, At Your Own Dock.</p><a>LEARN MORE</a>
  </div>
  <p class="tagline">Good Boats. Great People. Brighter Tomorrows.</p>
</section>

<footer class="footer">
  <div class="brand-badge">Captain Rowan's Boat Training &amp; Charters</div>
  <div class="socials"><span></span><span></span><span></span></div>
  <p class="f-head" style="left:660px">NAVIGATION</p>
  <div class="f-links"><div>Home</div><div>Services</div><div>Boating Aids</div><div>Gallery</div><div>About</div><div>Contact</div></div>
  <p class="f-head" style="left:922px;top:45px">CONTACT US</p>
  <div class="contact-row" style="top:64px"><span class="ic"><svg width="14" height="14" viewBox="0 0 14 14"><path d="M3 1l2 3-1.5 1.5a8 8 0 0 0 5 5L10 9l3 2-1.5 2.5C6 13 1 8 .5 2.5z" fill="#fff"/></svg></span><b style="font-size:14px">(555) 310-4827</b></div>
  <div class="contact-row" style="top:100px"><span class="ic"><svg width="14" height="10" viewBox="0 0 14 10"><rect x=".5" y=".5" width="13" height="9" fill="none" stroke="#fff"/><path d="M.5 .5l6.5 5 6.5-5" fill="none" stroke="#fff"/></svg></span><span style="text-decoration:underline">service@helmready-mail.com</span></div>
  <div class="contact-row" style="top:135px"><span class="ic"><svg width="12" height="15" viewBox="0 0 12 15"><path d="M6 14S1 8 1 5.5a5 5 0 0 1 10 0C11 8 6 14 6 14z" fill="none" stroke="#fff" stroke-width="1.3"/><circle cx="6" cy="5.5" r="1.8" fill="#fff"/></svg></span><span style="font-size:11px">Marlow Cove, Florida</span></div>
  <p class="copy">© 2026 Captain Rowan's Boat Training &amp; Charters, LLC. All rights reserved. &nbsp;|&nbsp; Privacy Policy &nbsp;&nbsp;|&nbsp;&nbsp; Terms and Conditions</p>
</footer>

</body>
</html>
```